Business Card - Rebranding for Consulting Firm

We are renaming and rebranding our consulting firm and need to raise the level of quality of our cards as part of that effort. We consult to leading high tech, life science and other innovation sector companies.

Need a two-sided business card design.

Side 1: (a) Company logo (b) tag line: Optimize Your Investment in Talent (c) Name (d) Title (e) Phone 1: Office (f) Phone 2: Mobile (g) email: person@HollowmereAdvisory.com

Side 2: Two lines of text: (a) Growth is Imperative. Change is Constant. Talent Executes Strategy. (b) We help you excel at all three.

Target Market(s)

Business and human resources executives and senior managers

Industry/Entity Type

Management Consulting

Contact Information for Business Card

Font styles to use
Sans Serif

Requirements
Must have
• clean, not too busy, but with a bit of creativity. Stick to the colors used in the attached logo
• appeal to high tech, life science companies
Nice to have
• prefer white background

```html
<!DOCTYPE html>
<html lang="en">
<head>
<meta charset="utf-8">
<title>Hollowmere Advisory – Business Card</title>
<link rel="stylesheet" href="https://fonts.googleapis.com/css2?family=Roboto:wght@400;500&family=Roboto+Condensed:wght@400&family=Exo+2:wght@700&display=swap">
<style>
  :root {
    --brand-blue: #0b5d95;
    --band-grey: #5f7285;
    --text-grey: #5c6670;
    --rule-grey: #7d8893;
    --card-white: #fbfbfb;
    --stage: #dcdcdc;
  }
  * { margin: 0; padding: 0; box-sizing: border-box; }
  html, body { width: 1200px; height: 576px; overflow: hidden; }
  body {
    position: relative;
    background: var(--stage);
    font-family: "Roboto", Arial, sans-serif;
  }
  .card {
    position: absolute;
    top: 139px;
    height: 293px;
    background: var(--card-white);
    border-radius: 8px;
    box-shadow: 0 2px 6px rgba(0,0,0,0.18);
    overflow: hidden;
  }
  .card--back { left: 82px; width: 484px; }
  .card--front { left: 602px; width: 480px; height: 290px; }

  .brand {
    position: absolute;
    display: flex;
    align-items: center;
    gap: 7px;
    color: var(--brand-blue);
    font-family: "Roboto", Arial, sans-serif;
    font-weight: 400;
    white-space: nowrap;
  }
  .brand__mark { width: 13px; height: 13px; background: var(--brand-blue); }
  .card--back .brand { left: 0; right: 0; top: 77px; justify-content: center; font-size: 25px; }
  .card--back .brand__mark { width: 17px; height: 17px; }
  .card--front .brand { right: 20px; top: 40px; font-size: 20px; }

  .motto {
    position: absolute;
    left: 64px; top: 190px;
    width: 354px; height: 33px;
    border: 1px solid var(--rule-grey);
    border-top: none;
    text-align: center;
    color: var(--brand-blue);
  }
  .motto::before, .motto::after {
    content: ""; position: absolute; top: 0;
    border-top: 1px solid var(--rule-grey); width: 18px;
  }
  .motto::before { left: 0; }
  .motto::after { right: 0; }
  .motto__lead {
    position: absolute; left: 0; right: 0; top: -8px;
    font-family: "Roboto Condensed", "Arial Narrow", sans-serif;
    font-size: 11.3px; line-height: 15px;
    white-space: nowrap;
  }
  .motto__sub {
    position: absolute; left: 0; right: 0; top: 11px;
    font-size: 13px;
  }

  .person { position: absolute; left: 22px; top: 40px; }
  .person__name {
    font-family: "Exo 2", Arial, sans-serif;
    font-weight: 700; font-size: 19px;
    color: var(--brand-blue); letter-spacing: 0.3px;
  }
  .person__title { font-size: 12px; color: var(--text-grey); margin-top: 1px; }

  .contacts { position: absolute; left: 24px; top: 156px; list-style: none; }
  .contacts li {
    display: flex; align-items: center; gap: 10px;
    font-size: 12.5px; color: var(--text-grey);
    height: 17.3px;
  }
  .contacts svg { width: 10px; height: 10px; fill: var(--brand-blue); }
  .contacts .highlight { color: var(--brand-blue); }

  .accent-band {
    position: absolute; left: 0; right: 0; bottom: 0; height: 64px;
    background: linear-gradient(90deg, var(--band-grey) 0%, var(--brand-blue) 55%);
  }
  .slogan {
    position: absolute; right: 20px; top: 236px;
    text-align: right; color: #fff;
    font-size: 13px; line-height: 18px;
  }
</style>
</head>
<body>
  <section class="card card--back">
    <div class="brand"><span class="brand__mark"></span>Hollowmere Advisory LLC</div>
    <div class="motto">
      <div class="motto__lead">Growth is Imperative. Change is Constant. Talent Executes Strategy.</div>
      <div class="motto__sub">We help you excel at all three.</div>
    </div>
  </section>

  <section class="card card--front">
    <div class="accent-band" role="img" aria-label="Decorative blue and grey wave band"></div>

    <div class="person">
      <div class="person__name">Daniel Reyes</div>
      <div class="person__title">Managing Director</div>
    </div>
    <div class="brand"><span class="brand__mark"></span>Hollowmere Advisory LLC</div>

    <ul class="contacts">
      <li><svg viewBox="0 0 10 10"><rect x="2" y="0" width="6" height="10" rx="1"/><rect x="3" y="1.5" width="4" height="6" fill="#fff"/></svg>+100 200 3000</li>
      <li><svg viewBox="0 0 10 10"><path d="M0 3 Q5 0 10 3 L9 4.5 L7 4 L7 3 Q5 2.4 3 3 L3 4 L1 4.5 Z"/><rect x="1.5" y="5" width="7" height="4" rx="1"/></svg>+400 500 6000</li>
      <li><svg viewBox="0 0 10 10"><rect x="0" y="1.5" width="10" height="7"/><path d="M0.5 2 L5 5.5 L9.5 2" stroke="#fff" fill="none"/></svg>person@HollowmereAdvisory.com</li>
      <li><svg viewBox="0 0 10 10"><circle cx="5" cy="5" r="5"/><path d="M0 5 H10 M5 0 V10 M5 0 Q1.5 5 5 10 M5 0 Q8.5 5 5 10" stroke="#fff" stroke-width="0.8" fill="none"/></svg><span>www.<span class="highlight">HollowmereAdvisory</span>.com</span></li>
    </ul>

    <div class="slogan">Optimize Your<br>Investment in Talent</div>
  </section>
</body>
</html>
```